FinTech company looking to revamp and expand client-facing interface for our financial models

Halvern Ledgerworks currently has a very simple website that allows clients to interact with our financial models. We are looking to completely redesign the current site and add several extra pages to provide extra functionality. We want the design to have a modern, slick feel, that will work on both a desktop or a tablet. It should be straightforward for clients to move between different pages at any time, and clear from the layout how to interact with the more advanced features. We have included screenshots of existing pages in the attached design brief, as well as sketches of the functionality required by the new pages, but can't provide a direct link to the current site.
Target Market(s)
Professional investors that will be paying to access the interface
Industry/Entity Type
Finance
Number of Pages Required
4 page
Colors
Designer to choose colors to be used in the design.
Look and feel
Each slider illustrates characteristics of the customer's brand and the style your logo design should communicate.

```html
<!DOCTYPE html>
<html lang="en">
<head>
<meta charset="utf-8">
<title>Halvern Ledgerworks – ETF Pairs</title>
<link rel="stylesheet" href="https://fonts.googleapis.com/css2?family=Open+Sans:wght@400;600;700&family=Roboto+Condensed:wght@400;500&display=swap">
<style>
:root{
  --navy:#0b3566;
  --cyan:#1ba0d8;
  --head-grey:#a9a9a9;
  --frame:#e4e4e4;
  --white:#ffffff;
  --ink:#111111;
  --line:#e2e2e2;
  --row-light:#f7f7f7;
  --row-dark:#e6e6e6;
  --tab-grey:#c8c8c8;
}
*{box-sizing:border-box;margin:0;padding:0}
html,body{width:1200px;height:715px;overflow:hidden;background:var(--frame)}
body{font-family:"Open Sans",Arial,sans-serif;color:var(--ink);position:relative}
.app{position:absolute;left:14px;top:14px;width:1172px;height:687px;background:var(--white)}
.topbar{position:absolute;left:0;top:0;width:100%;height:55px;background:var(--white);border-bottom:1px solid var(--line)}
.brand{position:absolute;left:53px;top:0;height:55px;line-height:55px;font-weight:700;font-size:17px;letter-spacing:.2px}
.nav-item{position:absolute;top:0;height:55px;display:flex;align-items:center;justify-content:center;gap:7px;font-weight:700;font-size:12.5px;border-right:1px solid var(--line)}
.nav-item.active{background:var(--navy);color:var(--white);border-right-color:var(--navy)}
.nav-item svg{width:20px;height:20px}
.band{position:absolute;left:0;top:55px;width:100%;height:88px;background:linear-gradient(#d6d6d6,#ededed 60%,#f3f3f3)}
.tab{position:absolute;bottom:0;height:32px;background:var(--white);border-radius:4px 4px 0 0;display:flex;align-items:center;justify-content:center;font-weight:600;font-size:12px}
.tab.tall{height:42px;padding-bottom:6px}
.tab.active{height:51px;background:var(--navy);color:var(--white);padding-bottom:14px}
.tab.more{background:var(--tab-grey);border-radius:4px 4px 0 0}
.tab.add{background:var(--navy)}
.filters{position:absolute;left:53px;top:181px;width:1068px;height:28px;font-size:15px}
.filter{position:absolute;top:0;height:28px;display:flex;align-items:center}
.filter b{font-weight:700;margin-left:12px;margin-right:12px}
.filter input{width:166px;height:29px;border:1px solid #cfcfcf;border-radius:4px;box-shadow:0 1px 2px rgba(0,0,0,.15);font:15px "Open Sans",Arial,sans-serif;padding-left:9px;color:var(--ink)}
.export{position:absolute;right:0;top:0;height:28px;display:flex;align-items:center;gap:8px;color:var(--navy);font-weight:700;font-size:15.5px}
.models{position:absolute;left:51px;top:244px;width:1070px;border-collapse:collapse;font-family:"Roboto Condensed","Arial Narrow",sans-serif;font-size:15px;table-layout:fixed}
.models th{height:65px;color:var(--white);font-family:"Open Sans",Arial,sans-serif;font-weight:600;font-size:15px;background:var(--head-grey);border-right:1px solid #bcbcbc}
.models th.key{background:var(--cyan);border-right-color:#3bb0e0}
.models th:first-child{border-top-left-radius:6px}
.models th:last-child{border-top-right-radius:6px;border-right:none}
.models td{height:64px;padding-left:12px;border-right:1px solid var(--line);line-height:1.25}
.models td:last-child{border-right:none}
.models tr:nth-child(odd) td{background:var(--row-light)}
.models tr:nth-child(even) td{background:var(--row-dark)}
.models td.num{padding-left:10px}
</style>
</head>
<body>
<div class="app">
  <header class="topbar">
    <div class="brand">HALVERN</div>
    <div class="nav-item active" style="left:166px;width:83px">250D</div>
    <div class="nav-item" style="left:249px;width:83px">83D</div>
    <div class="nav-item" style="left:332px;width:83px">42D</div>
    <div class="nav-item active" style="left:697px;width:129px">
      <svg viewBox="0 0 24 24" fill="none" stroke="#fff" stroke-width="2"><path d="M3 11 12 3l9 8"/><path d="M5 10v10h5v-6h4v6h5V10"/></svg>MODELS</div>
    <div class="nav-item" style="left:826px;width:164px;border-left:1px solid var(--line)">
      <svg viewBox="0 0 24 24" fill="#333"><circle cx="12" cy="12" r="3"/><circle cx="12" cy="4" r="1.6"/><circle cx="12" cy="20" r="1.6"/><circle cx="4" cy="12" r="1.6"/><circle cx="20" cy="12" r="1.6"/><circle cx="6.3" cy="6.3" r="1.6"/><circle cx="17.7" cy="17.7" r="1.6"/><circle cx="17.7" cy="6.3" r="1.6"/><circle cx="6.3" cy="17.7" r="1.6"/></svg>SENSITIVITIES</div>
    <div class="nav-item" style="left:990px;width:155px;border-right:none">
      <svg viewBox="0 0 24 24" fill="none" stroke="#111" stroke-width="1.8"><path d="M12 3l2.7 5.8 6.3.7-4.7 4.3 1.3 6.2L12 16.9 6.4 20l1.3-6.2L3 9.5l6.3-.7z"/></svg>FAVOURITES</div>
  </header>

  <nav class="band">
    <div class="tab" style="left:51px;width:143px">EQUITIES</div>
    <div class="tab" style="left:198px;width:143px">ETFS</div>
    <div class="tab tall" style="left:346px;width:143px">PAIRS</div>
    <div class="tab active" style="left:494px;width:143px">ETF PAIRS</div>
    <div class="tab tall" style="left:641px;width:143px">FACTORS</div>
    <div class="tab" style="left:789px;width:143px">NEW TAB TITLE #1</div>
    <div class="tab" style="left:937px;width:143px">NEW TAB TITLE #2</div>
    <div class="tab more" style="left:1084px;width:37px">
      <svg width="12" height="16" viewBox="0 0 12 16" fill="none" stroke="#fff" stroke-width="3"><path d="M3 2l6 6-6 6"/></svg></div>
    <div class="tab add" style="left:1126px;width:37px">
      <svg width="22" height="22" viewBox="0 0 22 22" fill="none" stroke="#fff" stroke-width="1.8"><circle cx="11" cy="11" r="9.5"/><path d="M11 6v10M6 11h10"/></svg></div>
  </nav>

  <section class="filters">
    <label class="filter" style="left:0">Quality <b>Threshold:</b><input type="text" value="-10"></label>
    <label class="filter" style="left:380px"><b style="margin-left:0;margin-right:4px">Abs.</b> Stat <b>Threshold:</b><input type="text" value="-10"></label>
    <div class="export">
      <svg width="24" height="22" viewBox="0 0 24 22" fill="none" stroke="#0b3566" stroke-width="2"><path d="M10 4H3v15h15v-6"/><path d="M8 14c1-5 5-8 11-8"/><path d="M16 2l4 4-4 4"/></svg>Export</div>
  </section>

  <table class="models">
    <colgroup><col style="width:92px"><col style="width:102px"><col style="width:106px"><col style="width:106px"><col span="8" style="width:83px"></colgroup>
    <thead><tr>
      <th class="key">ID <svg width="10" height="7" viewBox="0 0 10 7" fill="none" stroke="#fff" stroke-width="2"><path d="M1 1l4 4 4-4"/></svg></th>
      <th class="key">Sector</th><th class="key">Time</th>
      <th>Quality</th><th>Stat 1</th><th>Stat 2</th><th>Stat 3</th><th>Stat 4</th><th>Stat 5</th><th>Stat 6</th><th>Stat 7</th><th>Stat 8</th>
    </tr></thead>
    <tbody>
      <tr><td>Model 1</td><td>Materials</td><td>2019-07-03<br>12:15:00.000</td><td class="num" style="padding-left:24px">30.2288</td><td class="num">2.01574</td><td class="num">23.305</td><td class="num">-0.149368</td><td class="num">22.3054</td><td class="num">4.63714</td><td class="num">0.945706</td><td class="num">2.81949</td><td class="num">2.60858</td></tr>
      <tr><td>Model 2</td><td>Industrials</td><td>2019-07-03<br>12:15:00.000</td><td class="num" style="padding-left:24px">32.8694</td><td class="num">0.87307</td><td class="num">32.185</td><td class="num">-0.033692</td><td class="num">33.9911</td><td class="num">11.5693</td><td class="num">-0.472968</td><td class="num">-0.830458</td><td class="num">6.80646</td></tr>
      <tr><td>Model 3</td><td>Consumer Discretionary</td><td>2019-07-03<br>12:15:00.000</td><td class="num" style="padding-left:24px">1.66002</td><td class="num">-0.569222</td><td class="num">159.814</td><td class="num">0.0252328</td><td class="num">172.616</td><td class="num">10.2875</td><td class="num">-0.750396</td><td class="num">-0.385309</td><td class="num">4.69146</td></tr>
      <tr><td>Model 4</td><td>Information Technology</td><td>2019-07-03<br>12:15:00.000</td><td class="num" style="padding-left:24px">45.6856</td><td class="num">0.412148</td><td class="num">202.488</td><td class="num">0.0084923</td><td class="num">205.834</td><td class="num">11.9094</td><td class="num">-0.137913</td><td class="num">0.449595</td><td class="num">3.85106</td></tr>
      <tr><td>Model 5</td><td>Information Technology</td><td>2019-07-03<br>12:15:00.000</td><td class="num" style="padding-left:24px">75.7733</td><td class="num">7.06728</td><td class="num">188.605</td><td class="num">0.016913</td><td class="num">161.665</td><td class="num">3.82241</td><td class="num">0.981019</td><td class="num">1.29847</td><td class="num">3.34927</td></tr>
    </tbody>
  </table>
</div>
</body>
</html>
```